Lantern Hour book needs a cover design

I need a front and back cover design that demonstrates a strong sense of possibility that trust can be repaired even if things look bleak. Repairing trust is difficult, but this book is full of wisdom, proven strategies, and doctoral research to help people strengthen relationships and improve trust. It can help any group: business, nonprofit, education, service. Showing diversity of groups and people is very important. For the cover title, there should be a play on words: "Lantern Hour: Is it? Possible" should have the words "is it?" crossed out and the words "It IS! should be replaced there in a striking way. Perhaps in red ink. For publishing purposes, book will be titled Lantern Hour: It IS Possible! Please see the attachment for an example. The book layout is approximately 260 pages.

Target Market(s)

A business self-help book, but the target is any person in a group that feels they have lost trust in each other. It can be just a normal person struggling in a volunteer group they are a part of, or a supervisor whose group is not working well together. It can be a leader who just wants their group to be stronger.

Industry/Entity Type

Business Management

Font styles to use
Other font styles liked:
• Allise - I believe is being used on the interior of the book for the title page and headings

Requirements
Must have
• Show hope and possibility in the midst of difficulty. Must have a play on the words in the title "Lantern Hour: Is it? Possible" with crossing out "is it?" with "It IS!" (see attached example) Must include the author's name: Marla Quinby, PhD Must include a smaller tagline: "Proven Strategies to Help Groups Get Unstuck"
Nice to have
• Showing diverse people, or hands. Diverse kinds of groups - not just business. A colorful cover. Maybe show the complexity of trust when it is broken...broken pieces of trust that are then picked up and put together when people work together. Could show people (or images of hands) or other ways to show that it's a choice and it is possible to repair broken trust. I'd also like to convey a sense of a group - not just random people. That they have something at stake to work on repairing trust together and this book can help them.
Should not have
• If images of people are used, just showing one gender or race is not okay. Nor just binary choices: like an image containing one man and one woman, or one white person and one person of color - otherwise it seems that the book on Lantern Hour is about race or gender relations.

```html
<!DOCTYPE html>
<html lang="en">
<head>
<meta charset="utf-8">
<title>Lantern Hour: It IS Possible! — Book Cover</title>
<link href="https://fonts.googleapis.com/css2?family=Archivo+Black&family=Bungee+Inline&family=Montserrat:wght@400;800&family=Oswald:wght@600&display=swap" rel="stylesheet">
<style>
  :root {
    --paper: #ffffff;
    --navy: #0b3f86;
    --banner: #0f3a5a;
    --banner-edge: #1d1d1d;
    --red: #a3141a;
    --pale-blue: #a4c5e8;
    --strike: #3a3a3a;
    --green-text: #1f5a22;
    --white: #ffffff;
  }
  html, body {
    margin: 0;
    padding: 0;
    overflow: hidden;
    background: var(--paper);
  }
  .cover {
    position: relative;
    width: 800px;
    height: 1200px;
    overflow: hidden;
    background: var(--paper);
  }
  .tagline {
    position: absolute;
    top: 30px;
    left: 0;
    width: 800px;
    margin: 0;
    text-align: center;
    font-family: "Montserrat", Arial, sans-serif;
    font-weight: 800;
    font-size: 17px;
    letter-spacing: 3.2px;
    color: var(--navy);
    text-transform: uppercase;
  }
  .hero-art {
    position: absolute;
    left: 85px;
    top: 195px;
    width: 600px;
    height: 465px;
    background:
      radial-gradient(ellipse at 40% 35%, rgba(240,240,240,0.95) 0 18%, transparent 40%),
      linear-gradient(90deg, #c8e64a 0%, #7bd63a 35%, #25c25a 60%, #18b8b0 82%, #1a4fa0 100%);
    opacity: 0.55;
    border-radius: 4px;
  }
  .group-list {
    position: absolute;
    left: 700px;
    top: 655px;
    width: 510px;
    margin: 0;
    transform: rotate(-90deg);
    transform-origin: 0 0;
    font-family: "Oswald", Arial, sans-serif;
    font-weight: 600;
    font-size: 13.5px;
    letter-spacing: 0.2px;
    color: var(--green-text);
    text-transform: uppercase;
    white-space: nowrap;
  }
  .title-block {
    position: absolute;
    left: 0;
    top: 660px;
    width: 800px;
    height: 320px;
  }
  .title-main {
    font-family: "Bungee Inline", Impact, sans-serif;
    fill: var(--navy);
  }
  .title-answer {
    font-family: "Archivo Black", Arial, sans-serif;
  }
  .answer-emphasis { fill: var(--red); }
  .answer-word { fill: var(--navy); }
  .title-question {
    font-family: "Archivo Black", Arial, sans-serif;
    fill: var(--pale-blue);
  }
  .strike-line {
    stroke: var(--strike);
    stroke-width: 2;
  }
  .author-banner {
    position: absolute;
    left: 0;
    top: 1030px;
    width: 800px;
    height: 100px;
  }
  .banner-shape {
    fill: var(--banner);
    stroke: var(--banner-edge);
    stroke-width: 5;
    stroke-linejoin: round;
  }
  .author-name {
    font-family: "Montserrat", Arial, sans-serif;
    font-weight: 400;
    font-size: 50px;
    letter-spacing: 2px;
    fill: var(--white);
  }
</style>
</head>
<body>
<main class="cover">
  <p class="tagline">Proven Strategies to Help Groups Get Unstuck</p>

  <div class="hero-art" role="img" aria-label="Illustration of two white figures climbing a rising rainbow-coloured bar chart, the higher figure reaching down to help the other up"></div>

  <p class="group-list">Repair Your Relationship • Education • Nonprofit • Business • Service</p>

  <svg class="title-block" viewBox="0 0 800 320" aria-label="Lantern Hour: It IS Possible">
    <text class="title-main" x="72" y="102" font-size="96" textLength="658" lengthAdjust="spacingAndGlyphs">LANTERN HOUR</text>
    <text class="title-answer" x="90" y="222" font-size="78" textLength="545" lengthAdjust="spacingAndGlyphs"><tspan class="answer-emphasis">IT IS</tspan> <tspan class="answer-word">POSSIBLE</tspan></text>
    <text class="title-question" x="76" y="297" font-size="66" textLength="620" lengthAdjust="spacingAndGlyphs">IS IT POSSIBLE ?</text>
    <line class="strike-line" x1="74" y1="280" x2="716" y2="262"/>
    <line class="strike-line" x1="74" y1="262" x2="716" y2="280"/>
  </svg>

  <svg class="author-banner" viewBox="0 0 800 100">
    <path class="banner-shape" d="M -10 6 L 640 6 L 688 50 L 640 94 L -10 94 Z"/>
    <text class="author-name" x="330" y="68" text-anchor="middle">MARLA QUINBY, PhD</text>
  </svg>
</main>
</body>
</html>
```